Lotvantage.com Webpage Design

Design Brief for lotvantage.com (Copy of Brief also in attached Word file)

Name of Website- lotvantage.com (existing logo and look & feel of website to be changed)

Logo - Finalised. The logo files are attached with the brief as “logo.jpeg”. The “Blue- Grey” version of the logo is for use on lighter backgrounds and the “Orange-White” version of the logo is for use on darker backgrounds. (A full Black version of the logo is also attached). Both versions may be used in different parts of the website. All attached files are in .png format.
Status - The website in functional and is undergoing user trials. However, we want to improve the look & feel of the website so at it seems
a. cotemporary,
b. Easy to Navigate
c. professional and
d. Vibrant.

Please visit ‘lotvantage.com’ to check out the website and its functionalities – please use it only as a reference for the features & functions to be provided, however the designer should use a ‘Free Hand’ in designing the composition of various parts of the webpage without getting too influenced by the existing design

Objective of the Website ‘lotvantage.com –
a. It is a portal focussed on listing of ‘Retail’ specific real-estate properties by developers, owners and realty brokers. The properties shall listed under the following four categories-
i. Retail Malls
ii. Shopping Complexes
iii. High-street shops
iv. Retail Warehouses
*refer lotvantage.com for better clarity

b. The abovementioned properties shall be listed either for ‘Sale’ or ‘rent\lease’ or both

c. Users shall visit the site in case they wish to acquire a retail \ shop space either on ‘sale’ or ‘rent’. These Users would be able to specify the ‘Search Criteria’ through the tool-bars provided on the website – the ‘Search Criteria’ shall comprise of ‘Type of space category’, ‘City’, ‘Locality’, transaction type ie ‘Rent \ Sale’ and ‘Area Range’

d. The main revenue model for the website shall be listing fee ( or advertising charges ) payable by those listing their properties on the website.

Three Main Pages of Website (lotvantage.com) that need to be designed -
a. Main Home Page (visit the web link - http://lotvantage.com/ ) - The main home page has the “Search Toolbar” for specifying of Search Criteria by the User. It shall also have the following features & functions-
i. Main Advertising Banner
ii. Featured Projects
iii. New Launches
iv. Toolbar with buttons – ‘Advertise with Us’, ‘Listings Alert’, ‘Lot Mavens’, ‘Advertiser Login’

b. Property Listings Page (visit the web link - http://lotvantage.com/gurgaon-in-india ) - The List of property options that match the Criteria specified by the ‘User’ get displayed on this page.

c. Property Detail Page - When the ‘User’ clicks on the “More….” Button on the ‘Property Listings Page’ (given in point b. above) the web page with the details of the property opens. (For Example – visit the web link - http://lotvantage.com/brevo-Shopping-Complex-brevo-quadrel-gurgaon-636 )

Note:- Please refer to attached ‘Shopping’ related images the designer may use them on the website to provide a look & feel of retail if required – either separately or rotate in a single window

Target Market(s)

Retailers & Investors looking for retail space, Real Estate Brokers, Developers

Industry/Entity Type

Advertising

Number of Pages Required

3 page

Requirements
Must have
• Refer to existing site lotvantage.com -- all the existing functionalities are a must have.
Nice to have
• The Designer may use the retail related images on the website if required for making it more vibrant. Refer attached images Shopping(1-6).jpg

```html
<!DOCTYPE html>
<html lang="en">
<head>
<meta charset="utf-8">
<title>Lotvantage.com – Retail Space Portal</title>
<link href="https://fonts.googleapis.com/css2?family=Open+Sans:wght@400;600;700;800&display=swap" rel="stylesheet">
<style>
:root{
  --blue:#0f9bf2;
  --blue-dark:#0a86d6;
  --ink:#333;
  --muted:#8a8a8a;
  --line:#e3e3e3;
  --topbar:#1f1f1f;
  --panel:#f3f3f3;
  --white:#fff;
}
*{box-sizing:border-box;margin:0;padding:0}
html,body{width:1200px;height:2496px;overflow:hidden}
body{font-family:"Open Sans",Arial,sans-serif;color:var(--ink);background:var(--white);position:relative}
.wrap{width:854px;margin-left:173px;position:relative}

/* top bar */
.topbar{height:31px;background:var(--topbar);color:#bbb;font-size:10px}
.topbar .wrap{display:flex;justify-content:space-between;height:31px;align-items:center}
.city-links,.account-links{display:flex;height:31px}
.city-links a,.account-links a{color:#bbb;text-decoration:none;padding:0 20px;display:flex;align-items:center;border-right:1px solid #333}
.city-links a:first-child,.account-links a:first-child{border-left:1px solid #333}

/* header */
.site-header{height:98px}
.site-header .wrap{display:flex;justify-content:space-between;align-items:center;height:98px}
.brand{display:flex;align-items:center;gap:10px}
.brand-dot{width:34px;height:34px;border-radius:50%;background:var(--blue)}
.brand-name{font-size:30px;font-weight:700;color:var(--blue);line-height:1}
.brand-tag{font-size:8px;font-weight:700;color:#555;letter-spacing:.5px;margin-top:3px}
.header-tools{display:flex;height:60px}
.tool{width:156px;text-align:center;border-left:1px solid var(--line);display:flex;flex-direction:column;align-items:center;justify-content:center}
.tool:first-child{border-left:none}
.tool svg{width:20px;height:20px;margin-bottom:3px}
.tool-title{font-size:13px;font-weight:600;color:var(--blue)}
.tool-sub{font-size:9px;color:#555}

/* hero */
.hero{height:395px;position:relative;background:linear-gradient(180deg,#dfe6ec 0%,#c9d3da 35%,#b39a7e 62%,#6f7f52 82%,#4b6a2c 100%)}
.hero-title{position:absolute;top:100px;left:0;width:100%;text-align:center;font-size:52px;font-weight:800;color:#fff;line-height:58px;letter-spacing:.5px;text-shadow:0 2px 4px rgba(0,0,0,.6)}
.hero-arrow{position:absolute;top:171px;width:54px;height:54px;border:2px solid rgba(255,255,255,.8);border-radius:50%}
.hero-arrow.prev{left:50px}.hero-arrow.next{right:50px}
.hero-arrow svg{width:50px;height:50px}
.search-panel{position:absolute;left:173px;top:283px;width:854px;height:112px;background:rgba(255,255,255,.93);padding:21px 20px 0}
.search-row{display:flex;gap:17px;height:42px}
.field{border:1px solid #ddd;background:#fff;font-size:10px;color:#777;display:flex;align-items:center;justify-content:space-between;padding:0 12px}
.field .caret{border-left:4px solid transparent;border-right:4px solid transparent;border-top:4px solid #999}
.btn-search{background:var(--blue);color:#fff;font-size:11px;font-weight:700;display:flex;align-items:center;justify-content:center;gap:8px;width:123px;margin-left:3px}
.format-row{display:flex;align-items:center;margin-top:14px;font-size:10px;color:#555;gap:6px}
.format-row .link{color:var(--blue);margin-right:26px}
.check{display:flex;align-items:center;gap:8px;margin-right:40px;color:#777}
.check i{width:13px;height:13px;border:1px solid #bbb;background:#fff;display:block}

/* section titles */
.section-title{text-align:center;margin-top:40px}
.section-title h2{font-size:40px;font-weight:400;color:var(--ink);line-height:46px}
.section-title h2 b{color:var(--blue);font-weight:600}
.section-title p{font-size:18px;color:#666}
.formats{display:flex;gap:8px;margin-top:20px}
.format{width:208px}
.format .ph{height:200px}
.format h3{font-size:15px;font-weight:600;color:var(--blue);margin-top:16px}
.format p{font-size:12px;color:#777}

/* block headers */
.block-head{height:54px;background:var(--panel);display:flex;justify-content:space-between;align-items:center}
.block-tab{display:flex;height:54px;width:295px;background:var(--blue);color:#fff;align-items:center;font-size:18px;font-weight:600}
.block-tab .icon{width:68px;height:54px;background:var(--blue-dark);display:flex;align-items:center;justify-content:center;margin-right:40px}
.pager{display:flex;gap:30px;padding-right:20px}
.pager svg{width:14px;height:14px}

/* cards */
.grid{display:grid;grid-template-columns:repeat(3,271px);column-gap:21px;row-gap:23px;margin-top:29px}
.card{border:1px solid var(--line)}
.card .ph{height:206px;position:relative}
.card-body{padding:4px 14px 0}
.card-top{display:flex;justify-content:space-between;align-items:baseline}
.card-title{font-size:16px;font-weight:600;color:var(--blue)}
.card-city{font-size:12px;font-weight:700}
.card-type{font-size:11px;color:var(--muted)}
.card-meta{display:flex;justify-content:space-between;border-top:1px solid var(--line);margin:8px -14px 0;padding:10px 14px;font-size:11px}
.card-meta span{display:flex;align-items:center;gap:6px}
.btn-view{display:block;height:36px;background:var(--blue);color:#fff;text-align:center;line-height:36px;font-size:13px;font-weight:600;margin:0 -1px -1px}
.badge{position:absolute;left:14px;top:14px;width:56px;height:56px;border:2px solid #fff;border-radius:50%;color:#fff;font-size:11px;font-weight:700;display:flex;align-items:center;justify-content:center}
.shade{position:absolute;inset:0;background:rgba(0,0,0,.45)}
.zoom{position:absolute;left:110px;top:74px;width:50px;height:50px}

.grid-small{display:grid;grid-template-columns:repeat(4,208px);column-gap:7px;margin-top:27px}
.grid-small .ph{height:177px;position:relative}
.grid-small .card-body{padding:4px 8px 0}
.grid-small .card-title{font-size:12px}
.grid-small .card-city{font-size:10px}
.grid-small .card-type,.grid-small .card-loc{font-size:9px;color:#555}
.grid-small .card-type{color:var(--muted)}
.grid-small .btn-view{height:34px;line-height:34px;font-size:12px;margin-top:10px}
.grid-small .card{border:none}

/* footer */
.footer{position:absolute;top:2157px;left:0;width:1200px;height:245px;background:var(--panel)}
.footer .wrap{display:flex;gap:20px;padding-top:40px}
.fcol{width:200px}
.fcol h4{font-size:14px;font-weight:700;padding-bottom:8px;border-bottom:1px solid #bbb;margin-bottom:18px;letter-spacing:.3px}
.fcol p,.fcol li{font-size:11px;color:#888;line-height:16px;list-style:none}
.fcol li{line-height:23px}
.fcol .date{font-style:italic;margin-bottom:12px}
.btn-small{display:inline-block;background:var(--blue);color:#fff;font-size:10px;font-weight:600;padding:7px 24px;margin-top:10px}
.email{height:28px;border:1px solid #ccc;background:#fff;font-size:9px;color:#888;text-align:center;line-height:26px;margin-top:10px}
.btn-send{height:28px;background:var(--blue);color:#fff;font-size:10px;font-weight:600;text-align:center;line-height:28px}

.bottom{position:absolute;top:2402px;left:0;width:1200px;height:94px}
.bottom .wrap{display:flex;align-items:center;height:94px}
.bottom .brand-name{font-size:22px}
.bottom .brand-dot{width:26px;height:26px}
.copy{font-size:11px;color:#666;margin-left:30px}
.copy b{color:var(--blue);font-weight:400}
.social{margin-left:auto;display:flex;gap:12px}
.social i{width:28px;height:28px;border-radius:50%;background:#9a9a9a;display:block}
</style>
</head>
<body>

<div class="topbar">
  <div class="wrap">
    <nav class="city-links"><a>Bangalore</a><a>Chennai</a><a>Hyderabad</a><a>Gurgaon</a><a>More &#9662;</a></nav>
    <nav class="account-links"><a>Login</a><a>Register</a></nav>
  </div>
</div>

<header class="site-header">
  <div class="wrap">
    <div class="brand">
      <span class="brand-dot"></span>
      <div><div class="brand-name">lotvantage</div><div class="brand-tag">INDIA'S LEADING PORTAL FOR RETAIL SPACE</div></div>
    </div>
    <div class="header-tools">
      <div class="tool">
        <svg viewBox="0 0 24 24" fill="none" stroke="#0f9bf2" stroke-width="1.6"><path d="M12 2l3 6.5 7 .8-5.2 4.8 1.5 7L12 17.5 5.7 21l1.5-7L2 9.3l7-.8z"/></svg>
        <div class="tool-title">Lot Mavens</div><div class="tool-sub">Shop Search Services</div>
      </div>
      <div class="tool">
        <svg viewBox="0 0 24 24" fill="none" stroke="#0f9bf2" stroke-width="1.6"><path d="M6 17V11a6 6 0 0 1 12 0v6l2 2H4z"/><path d="M10 21h4"/></svg>
        <div class="tool-title">List Alert</div><div class="tool-sub">List Your Property Here</div>
      </div>
      <div class="tool">
        <svg viewBox="0 0 24 24" fill="none" stroke="#0f9bf2" stroke-width="1.6"><path d="M3 10v4h4l9 5V5L7 10z"/><path d="M19 9a4 4 0 0 1 0 6"/></svg>
        <div class="tool-title">Advertise with us</div><div class="tool-sub">Standard listing - FREE</div>
      </div>
    </div>
  </div>
</header>

<section class="hero" role="img" aria-label="Residential towers and a low-rise complex behind a green lawn under a pale sky">
  <h1 class="hero-title">INDIA'S LEADING PORTAL FOR<br>RENTAL SPACE !</h1>
  <span class="hero-arrow prev"><svg viewBox="0 0 50 50"><path d="M29 16l-9 9 9 9" fill="none" stroke="#fff" stroke-width="2"/></svg></span>
  <span class="hero-arrow next"><svg viewBox="0 0 50 50"><path d="M21 16l9 9-9 9" fill="none" stroke="#fff" stroke-width="2"/></svg></span>
  <form class="search-panel">
    <div class="search-row">
      <div class="field" style="width:119px">BOTH <span class="caret"></span></div>
      <div class="field" style="width:191px">CITY <span class="caret"></span></div>
      <div class="field" style="width:125px">LOCALITY <span class="caret"></span></div>
      <div class="field" style="width:186px">PROJECT NAME....</div>
      <div class="btn-search">SEARCH <svg width="12" height="12" viewBox="0 0 12 12"><circle cx="5" cy="5" r="3.8" fill="none" stroke="#fff" stroke-width="1.5"/><path d="M8 8l3 3" stroke="#fff" stroke-width="1.5"/></svg></div>
    </div>
    <div class="format-row">
      <span>Select Retail Format :</span><span class="link">Meaning of Retail Format</span>
      <label class="check"><i></i>Retail Malls</label>
      <label class="check"><i></i>Shopping Complex</label>
      <label class="check"><i></i>High Street Shops</label>
      <label class="check" style="margin-right:0"><i></i>Retail Warehouses</label>
    </div>
  </form>
</section>

<section class="wrap">
  <div class="section-title">
    <h2><b>Select</b> Retail <b>Format</b></h2>
    <p>Meaning of Retail Format</p>
  </div>
  <div class="formats">
    <div class="format"><div class="ph" role="img" aria-label="Bright mall atrium with potted plants" style="background:linear-gradient(160deg,#e8eae4,#9db48a)"></div><h3>Retail Malls</h3><p>Centrally Air-Conditioned</p></div>
    <div class="format"><div class="ph" role="img" aria-label="Multi-level shopping complex interior" style="background:linear-gradient(160deg,#d9cfc2,#7d6e62)"></div><h3>Shopping Complex</h3><p>Non Air-Conditioned Building</p></div>
    <div class="format"><div class="ph" role="img" aria-label="Warehouse showroom with display shelves" style="background:linear-gradient(160deg,#efece6,#4a423c)"></div><h3>Retail Warehouses</h3><p>Road Facing Retail</p></div>
    <div class="format"><div class="ph" role="img" aria-label="High street store with lit shelves" style="background:linear-gradient(160deg,#f3e9a8,#2c2a22)"></div><h3>High Street Shops</h3><p>Back-end Retail Storage</p></div>
  </div>
</section>

<section class="wrap" style="margin-top:56px">
  <div class="block-head">
    <div class="block-tab"><span class="icon"><svg width="20" height="20" viewBox="0 0 24 24"><path d="M12 2l3 6.5 7 .8-5.2 4.8 1.5 7L12 17.5 5.7 21l1.5-7L2 9.3l7-.8z" fill="#fff"/></svg></span>Featured Projects</div>
    <div class="pager"><svg viewBox="0 0 14 14"><path d="M9 2L4 7l5 5" fill="none" stroke="#ccc" stroke-width="1.5"/></svg><svg viewBox="0 0 14 14"><path d="M5 2l5 5-5 5" fill="none" stroke="#ccc" stroke-width="1.5"/></svg></div>
  </div>
  <div class="grid">
    <article class="card"><div class="ph" role="img" aria-label="Glass office tower" style="background:linear-gradient(160deg,#6fa7a0,#25403c)"><span class="shade"></span><span class="badge">RENT</span><svg class="zoom" viewBox="0 0 50 50"><circle cx="20" cy="20" r="13" fill="none" stroke="#0f9bf2" stroke-width="4"/><path d="M30 30l14 14" stroke="#0f9bf2" stroke-width="5"/></svg></div>
      <div class="card-body"><div class="card-top"><span class="card-title">The Grand Mall</span><span class="card-city">New Dehli</span></div><div class="card-type">Retail Malls</div>
      <div class="card-meta"><span><svg width="10" height="12" viewBox="0 0 10 12"><path d="M5 12S0 6.5 0 4a5 5 0 0 1 10 0c0 2.5-5 8-5 8z" fill="#555"/><circle cx="5" cy="4" r="1.6" fill="#fff"/></svg>Golf Course Road</span><span>More</span></div></div>
      <a class="btn-view">View The Listing</a></article>
    <article class="card"><div class="ph" role="img" aria-label="House with lawn under blue sky" style="background:linear-gradient(180deg,#4d8fd8,#a9c9e8 45%,#5d9a3a 70%,#3f7a22)"></div>
      <div class="card-body"><div class="card-top"><span class="card-title">The Grand Mall</span><span class="card-city">New Dehli</span></div><div class="card-type">Retail Malls</div>
      <div class="card-meta"><span><svg width="10" height="12" viewBox="0 0 10 12"><path d="M5 12S0 6.5 0 4a5 5 0 0 1 10 0c0 2.5-5 8-5 8z" fill="#555"/><circle cx="5" cy="4" r="1.6" fill="#fff"/></svg>Golf Course Road</span><span>More</span></div></div>
      <a class="btn-view">View The Listing</a></article>
    <article class="card"><div class="ph" role="img" aria-label="Stone and timber house on a lawn" style="background:linear-gradient(180deg,#3f82d2,#9cc1e6 40%,#b48a54 60%,#4f8a2c)"></div>
      <div class="card-body"><div class="card-top"><span class="card-title">The Grand Mall</span><span class="card-city">New Dehli</span></div><div class="card-type">Retail Malls</div>
      <div class="card-meta"><span><svg width="10" height="12" viewBox="0 0 10 12"><path d="M5 12S0 6.5 0 4a5 5 0 0 1 10 0c0 2.5-5 8-5 8z" fill="#555"/><circle cx="5" cy="4" r="1.6" fill="#fff"/></svg>Golf Course Road</span><span>More</span></div></div>
      <a class="btn-view">View The Listing</a></article>
    <article class="card"><div class="ph" role="img" aria-label="Glass office tower" style="background:linear-gradient(160deg,#e7eef0,#7fc3b0 50%,#3f8f7a)"></div>
      <div class="card-body"><div class="card-top"><span class="card-title">The Grand Mall</span><span class="card-city">New Dehli</span></div><div class="card-type">Retail Malls</div>
      <div class="card-meta"><span><svg width="10" height="12" viewBox="0 0 10 12"><path d="M5 12S0 6.5 0 4a5 5 0 0 1 10 0c0 2.5-5 8-5 8z" fill="#555"/><circle cx="5" cy="4" r="1.6" fill="#fff"/></svg>Golf Course Road</span><span>More</span></div></div>
      <a class="btn-view">View The Listing</a></article>
    <article class="card"><div class="ph" role="img" aria-label="Stone and timber house on a lawn" style="background:linear-gradient(180deg,#3f82d2,#9cc1e6 40%,#b48a54 60%,#4f8a2c)"></div>
      <div class="card-body"><div class="card-top"><span class="card-title">The Grand Mall</span><span class="card-city">New Dehli</span></div><div class="card-type">Retail Malls</div>
      <div class="card-meta"><span><svg width="10" height="12" viewBox="0 0 10 12"><path d="M5 12S0 6.5 0 4a5 5 0 0 1 10 0c0 2.5-5 8-5 8z" fill="#555"/><circle cx="5" cy="4" r="1.6" fill="#fff"/></svg>Golf Course Road</span><span>More</span></div></div>
      <a class="btn-view">View The Listing</a></article>
    <article class="card"><div class="ph" role="img" aria-label="Stone and timber house on a lawn" style="background:linear-gradient(180deg,#3f82d2,#9cc1e6 40%,#b48a54 60%,#4f8a2c)"></div>
      <div class="card-body"><div class="card-top"><span class="card-title">The Grand Mall</span><span class="card-city">New Dehli</span></div><div class="card-type">Retail Malls</div>
      <div class="card-meta"><span><svg width="10" height="12" viewBox="0 0 10 12"><path d="M5 12S0 6.5 0 4a5 5 0 0 1 10 0c0 2.5-5 8-5 8z" fill="#555"/><circle cx="5" cy="4" r="1.6" fill="#fff"/></svg>Golf Course Road</span><span>More</span></div></div>
      <a class="btn-view">View The Listing</a></article>
  </div>
</section>

<section class="wrap" style="margin-top:50px">
  <div class="block-head">
    <div class="block-tab"><span class="icon"><svg width="22" height="22" viewBox="0 0 24 24" fill="none" stroke="#fff" stroke-width="2"><circle cx="10" cy="8" r="4"/><path d="M3 21c0-4 3-7 7-7"/><path d="M17 13v8M13 17h8"/></svg></span>New Projects</div>
    <div class="pager"><svg viewBox="0 0 14 14"><path d="M9 2L4 7l5 5" fill="none" stroke="#ccc" stroke-width="1.5"/></svg><svg viewBox="0 0 14 14"><path d="M5 2l5 5-5 5" fill="none" stroke="#ccc" stroke-width="1.5"/></svg></div>
  </div>
  <div class="grid-small">
    <article class="card"><div class="ph" role="img" aria-label="House at dusk" style="background:linear-gradient(160deg,#5a5347,#1e1c18)"><span class="shade" style="background:rgba(0,0,0,.3)"></span><span class="badge">SALE</span><svg class="zoom" style="left:80px;top:62px;width:42px;height:42px" viewBox="0 0 50 50"><circle cx="20" cy="20" r="13" fill="none" stroke="#0f9bf2" stroke-width="4"/><path d="M30 30l14 14" stroke="#0f9bf2" stroke-width="5"/></svg></div>
      <div class="card-body"><div class="card-top"><span class="card-title">The Grand Mall</span><span class="card-city">New Dehli</span></div><div class="card-top"><span class="card-type">Retail Malls</span><span class="card-loc">Golf Course Road</span></div></div><a class="btn-view">View The Listing</a></article>
    <article class="card"><div class="ph" role="img" aria-label="House with lawn under blue sky" style="background:linear-gradient(180deg,#4d8fd8,#a9c9e8 45%,#5d9a3a 70%,#3f7a22)"></div>
      <div class="card-body"><div class="card-top"><span class="card-title">The Grand Mall</span><span class="card-city">New Dehli</span></div><div class="card-top"><span class="card-type">Retail Malls</span><span class="card-loc">Golf Course Road</span></div></div><a class="btn-view">View The Listing</a></article>
    <article class="card"><div class="ph" role="img" aria-label="Glass office tower" style="background:linear-gradient(160deg,#e7eef0,#7fc3b0 50%,#3f8f7a)"></div>
      <div class="card-body"><div class="card-top"><span class="card-title">The Grand Mall</span><span class="card-city">New Dehli</span></div><div class="card-top"><span class="card-type">Retail Malls</span><span class="card-loc">Golf Course Road</span></div></div><a class="btn-view">View The Listing</a></article>
    <article class="card"><div class="ph" role="img" aria-label="Large house with lawn" style="background:linear-gradient(180deg,#5c95d6,#b9cfe4 45%,#6d9a48 70%,#3f7a22)"></div>
      <div class="card-body"><div class="card-top"><span class="card-title">The Grand Mall</span><span class="card-city">New Dehli</span></div><div class="card-top"><span class="card-type">Retail Malls</span><span class="card-loc">Golf Course Road</span></div></div><a class="btn-view">View The Listing</a></article>
  </div>
</section>

<footer class="footer">
  <div class="wrap">
    <div class="fcol"><h4>LATEST NEWS</h4>
      <p>Post your Retail Space requirement with us and our.</p><p class="date">1 March, 2014</p>
      <p>Post your Retail Space requirement with us and our.</p><p class="date">1 March, 2014</p></div>
    <div class="fcol"><h4>EDITORS CHOICE</h4>
      <p>Post your Retail Space requirement with us and our experts shall get back with suitable options and even help you in your transaction.</p><a class="btn-small">MORE</a></div>
    <div class="fcol"><h4>USEFUL LINKS</h4>
      <ul><li>About Us</li><li>Privacy Policy</li><li>Terms of Use</li><li>Contact Us</li><li>Site Map</li></ul></div>
    <div class="fcol"><h4>OUR NEWSLETTER</h4>
      <p>Post your Retail Space requirement with us and our experts shall get back with suitable options!</p>
      <div class="email">EMAIL</div><div class="btn-send">SEND</div></div>
  </div>
</footer>

<div class="bottom">
  <div class="wrap">
    <div class="brand"><span class="brand-dot"></span><div class="brand-name">lotvantage</div></div>
    <p class="copy">Copyright © 2014, <b>Shopfront Central.com</b>. All rights reserved.</p>
    <div class="social"><i></i><i></i><i></i><i></i></div>
  </div>
</div>

</body>
</html>
```